Tallowmere Roofing Business Card

Need a business card with the logo that was designed here

Contact Information for Business Card

Name, Title, Phone, Email, Website, Company name

```html
<!DOCTYPE html>
<html lang="en">
<head>
<meta charset="utf-8">
<title>Tallowmere Roofing Business Card</title>
<link href="https://fonts.googleapis.com/css2?family=Open+Sans:wght@400;600;700&display=swap" rel="stylesheet">
<style>
  :root {
    --stage: #232323;
    --card-dark: #1e1e22;
    --brand-blue: #1377c6;
    --brand-blue-deep: #0e67b0;
    --steel-grey: #8f9296;
    --paper-white: #f4f6f8;
  }
  * { box-sizing: border-box; margin: 0; padding: 0; }
  html, body {
    width: 1200px; height: 780px; overflow: hidden;
    background: var(--stage);
    font-family: "Open Sans", Arial, sans-serif;
  }
  .stage {
    width: 1200px; height: 780px;
    display: flex; align-items: center; justify-content: center; gap: 40px;
  }
  .card {
    position: relative;
    width: 560px; height: 320px;
    border-radius: 4px; overflow: hidden;
    box-shadow: 0 14px 30px rgba(0,0,0,.45);
  }

  /* Front */
  .card-front { background: var(--card-dark); color: var(--paper-white); }
  .brand-lockup {
    position: absolute; left: 44px; top: 92px;
    display: flex; align-items: center; gap: 10px;
    color: var(--brand-blue); font-weight: 700; font-size: 22px; line-height: 1.15;
  }
  .brand-square { width: 14px; height: 14px; background: var(--brand-blue); flex: none; }
  .divider {
    position: absolute; left: 240px; top: 60px; width: 80px; height: 170px;
  }
  .person { position: absolute; left: 312px; top: 96px; }
  .person-name { font-size: 30px; font-weight: 700; line-height: 1.05; }
  .person-name .first { color: var(--brand-blue); }
  .person-name .last { color: var(--steel-grey); }
  .person-title { font-size: 13px; margin-top: 4px; }
  .contact-list { list-style: none; margin-top: 16px; font-size: 13px; }
  .contact-list li { display: flex; align-items: center; gap: 8px; margin-bottom: 5px; }
  .contact-list svg { width: 13px; height: 13px; flex: none; }
  .address-band {
    position: absolute; left: 0; bottom: 18px; width: 440px; height: 30px;
    background: var(--brand-blue);
    display: flex; align-items: center; padding-left: 26px;
    font-size: 13px; color: var(--paper-white);
  }
  .corner-mark {
    position: absolute; right: 0; bottom: 0; width: 120px; height: 70px;
    background: linear-gradient(135deg, var(--brand-blue) 0%, var(--steel-grey) 70%);
    clip-path: polygon(0 30%, 40% 30%, 40% 0, 100% 0, 100% 100%, 0 100%, 0 74%);
  }

  /* Back */
  .card-back { background: var(--brand-blue); }
  .back-pattern {
    position: absolute; inset: 0;
    background: linear-gradient(120deg, var(--brand-blue-deep) 0%, var(--brand-blue) 55%, #3a92d6 100%);
  }
  .back-lockup {
    position: absolute; left: 0; right: 0; top: 0; bottom: 0;
    display: flex; align-items: center; justify-content: center; gap: 10px;
    color: var(--paper-white); font-weight: 700; font-size: 24px;
  }
  .back-lockup .brand-square { background: var(--paper-white); }
</style>
</head>
<body>
<main class="stage">
  <section class="card card-front">
    <div class="brand-lockup"><span class="brand-square"></span><span>Tallowmere<br>Roofing</span></div>

    <svg class="divider" viewBox="0 0 80 170" aria-hidden="true">
      <line x1="78" y1="2" x2="2" y2="168" stroke="#c9ccd0" stroke-width="1"/>
    </svg>

    <div class="person">
      <h1 class="person-name"><span class="first">Daniel</span> <span class="last">Marsh</span></h1>
      <p class="person-title">Managing Director</p>
      <ul class="contact-list">
        <li>
          <svg viewBox="0 0 24 24" aria-hidden="true"><path fill="#1377c6" d="M6.6 10.8a15.1 15.1 0 0 0 6.6 6.6l2.2-2.2a1 1 0 0 1 1-.25 11.4 11.4 0 0 0 3.6.57 1 1 0 0 1 1 1V20a1 1 0 0 1-1 1A17 17 0 0 1 3 4a1 1 0 0 1 1-1h3.5a1 1 0 0 1 1 1c0 1.25.2 2.45.57 3.57a1 1 0 0 1-.25 1z"/></svg>
          (555) 214-6930
        </li>
        <li>
          <svg viewBox="0 0 24 24" aria-hidden="true"><rect x="2" y="5" width="20" height="14" rx="2" fill="#1377c6"/><path d="M3 6l9 7 9-7" fill="none" stroke="#1e1e22" stroke-width="1.6"/></svg>
          info@tallowmere.com
        </li>
        <li>
          <svg viewBox="0 0 24 24" aria-hidden="true"><circle cx="12" cy="12" r="10" fill="#1377c6"/><path d="M2 12h20M12 2c3 3 3 17 0 20M12 2c-3 3-3 17 0 20" fill="none" stroke="#1e1e22" stroke-width="1.4"/></svg>
          www.tallowmere.com
        </li>
      </ul>
    </div>

    <div class="address-band">4180 Larkspur Ave. Suite 310 Ashford Vale, TX 75900</div>
    <div class="corner-mark" role="img" aria-label="Brand roof symbol in blue and grey"></div>
  </section>

  <section class="card card-back">
    <div class="back-pattern" role="img" aria-label="Repeating brand roof pattern in tones of blue"></div>
    <div class="back-lockup"><span class="brand-square"></span><span>Tallowmere Roofing</span></div>
  </section>
</main>
</body>
</html>
```